看板デザインを依頼させて頂きます。看板は国道沿い(店前向かいに設置予定です。看板から「入りやすさ」「高級感」「やわらかさ」が伝わるイメージがあると嬉しいです。
昔ながらの寿司屋の厳ついイメージを払しょくし、且つ安い回転寿司のイメージでもありません。それ相応の高級かつ入りやすい感じが希望です。
記載項目
(例)
会社名:霞月寿司(家紋入り)
キャッチコピー:駐車場
看板サイズ:横 180㎝ x 縦 545㎝ /横 360㎝×縦123㎝
看板は2種類あり、縦でも横でも使用できるデザインを希望します。
希望イメージ
シンプル 複雑
単色 カラフル
暗い 明るい
日常 高級
遊び心 厳粛
未来的 伝統的
女性的 男性的
希望する色
バックを単色にする場合は、白か青でお願いします。単色以外なら複数色可能です。
納品ファイル
• 高解像度JPG (.jpg)
• イラストレーター形式 (.ai)
補足説明
昼夜問わず使用するので、夜でも目立つものを希望。
遠くからもわかるよう文字サイズは大きめを希望。
大漁旗みたいなデザインは希望せず、シンプルかつおしゃれな感じを希望。
家紋は必ず入れてください。
駐車場全体のイメージを添付しました。
看板のサイズ(2種類)のイメージを添付しました。
店内のイメージを添付しました。
現在の看板と家紋のデータです。
家紋は○の中に二が入っているやつです。

シンプル且つバランスのよいデザインが気に入りました。
色使いや文字のレイアウトのデザインも気に入りました。
社内選定の結果、こちらの提案を採用させて頂くことになりました。

たくさんの素晴らしい提案をいただきありがとうございました。
今回は、初めての仕事依頼で若干の不安もありましたが、それを打ち消すような素晴らしい提案をしてくださった事に、感謝申し上げます。

```html
<!DOCTYPE html>
<html lang="ja">
<head>
<meta charset="utf-8">
<title>霞月寿司 看板</title>
<link rel="stylesheet" href="https://fonts.googleapis.com/css2?family=Yuji+Boku&family=Dela+Gothic+One&display=swap">
<style>
  :root {
    --page: #ffffff;
    --sign-white: #ffffff;
    --panel-brown: #2d0d09;
    --accent-red: #8a2822;
    --name-blush: #f2c8b2;
    --mark-blush: #d9a48c;
  }
  html, body {
    margin: 0;
    padding: 0;
    width: 849px;
    height: 1200px;
    overflow: hidden;
    background: var(--page);
  }
  .canvas {
    position: relative;
    width: 849px;
    height: 1200px;
  }
  .sign {
    position: absolute;
    left: 235px;
    top: 38px;
    width: 373px;
    height: 1110px;
    background: var(--sign-white);
    box-shadow: 0 0 4px rgba(0,0,0,0.12);
  }
  .rule {
    position: absolute;
    left: 0;
    width: 100%;
    background: var(--accent-red);
  }
  .rule--top { top: 4px; height: 12px; }
  .rule--mid { top: 932px; height: 12px; }
  .rule--bottom { top: 1094px; height: 12px; }
  .name-panel {
    position: absolute;
    left: 0;
    top: 30px;
    width: 100%;
    height: 894px;
    background: var(--panel-brown);
  }
  .crest-mark {
    position: absolute;
    left: 108px;
    top: 58px;
    width: 80px;
    height: 80px;
    border-radius: 50%;
    background: var(--mark-blush);
  }
  .shop-name {
    position: absolute;
    left: 105px;
    top: 200px;
    width: 170px;
    margin: 0;
    writing-mode: vertical-rl;
    font-family: "Yuji Boku", serif;
    font-weight: 400;
    font-size: 150px;
    line-height: 170px;
    letter-spacing: -2px;
    color: var(--name-blush);
    -webkit-text-stroke: 3px var(--name-blush);
  }
  .parking-label {
    position: absolute;
    left: 0;
    top: 990px;
    width: 100%;
    margin: 0;
    text-align: center;
    font-family: "Dela Gothic One", sans-serif;
    font-size: 104px;
    line-height: 104px;
    letter-spacing: 4px;
    color: var(--panel-brown);
  }
</style>
</head>
<body>
<div class="canvas">
  <div class="sign">
    <div class="rule rule--top"></div>
    <div class="name-panel">
      <div class="crest-mark" aria-hidden="true"></div>
      <h1 class="shop-name">霞月寿司</h1>
    </div>
    <div class="rule rule--mid"></div>
    <p class="parking-label">駐車場</p>
    <div class="rule rule--bottom"></div>
  </div>
</div>
</body>
</html>
```